Baby Making Project

We need a poster design for a surrogacy/ivf clinic. We would like the poster to be used as office artwork and to say something like

'We came here as a couple, we left as a family'

The poster should have some family related picture in it, but not necessarily the standard mother, father and child image.
The services are used by many single and gay parents so we don't want to alienate anyone.
The poster should like modern, perhaps with the use of animals photo, or animated looking characters so you can't make out whether the parents are male/female.

```html
<!DOCTYPE html>
<html lang="en">
<head>
<meta charset="utf-8">
<title>We came here as a couple, we left as a family</title>
<link rel="stylesheet" href="https://fonts.googleapis.com/css2?family=Playfair+Display:ital,wght@1,700&family=Gelasio:wght@400&display=swap">
<style>
  :root {
    --page-bg: #ececec;
    --card-white: #ffffff;
    --mint: #a6dfc4;
    --teal: #6cc4b4;
    --lime: #bfe39a;
    --peach: #f7b18d;
    --coral: #e8454f;
    --magenta: #e0195a;
    --sun: #f6b13a;
    --lemon: #e3e66a;
    --text-white: #ffffff;
  }
  * { margin: 0; padding: 0; box-sizing: border-box; }
  html, body {
    width: 1200px;
    height: 900px;
    overflow: hidden;
    background: var(--page-bg);
  }
  .poster {
    position: absolute;
    left: 320px;
    top: 56px;
    width: 560px;
    height: 787px;
    background: var(--card-white);
    border-radius: 12px;
    padding: 10px;
  }
  .poster__art {
    position: relative;
    width: 100%;
    height: 100%;
    overflow: hidden;
    border-radius: 4px;
  }
  .poster__backdrop {
    position: absolute;
    inset: 0;
    background:
      radial-gradient(ellipse 60% 30% at 70% 75%, var(--lime) 0%, transparent 70%),
      radial-gradient(ellipse 50% 25% at 30% 35%, var(--teal) 0%, transparent 75%),
      linear-gradient(160deg, var(--mint) 0%, var(--teal) 45%, var(--lime) 100%);
  }
  .poster__family {
    position: absolute;
    left: 3px;
    top: 447px;
    width: 254px;
    height: 330px;
    border-radius: 120px 140px 0 0;
    background: linear-gradient(90deg, var(--lemon) 0%, var(--sun) 55%, var(--sun) 100%);
  }
  .line {
    position: absolute;
    font-family: "Gelasio", Georgia, serif;
    color: var(--text-white);
    white-space: nowrap;
  }
  .line--came {
    left: 58px;
    top: 150px;
    font-size: 27px;
    transform: rotate(-4deg);
  }
  .line--left {
    left: 243px;
    top: 336px;
    font-size: 35px;
    transform: rotate(-5deg);
  }
  .tag {
    position: absolute;
    display: flex;
    align-items: center;
    justify-content: center;
    border: 4px solid var(--card-white);
    font-family: "Playfair Display", Georgia, serif;
    font-style: italic;
    font-weight: 700;
    line-height: 1;
  }
  .tag--couple {
    left: 70px;
    top: 188px;
    width: 236px;
    height: 92px;
    background: var(--peach);
    color: var(--coral);
    font-size: 62px;
    transform: rotate(-4deg);
  }
  .tag--family {
    left: 212px;
    top: 390px;
    width: 286px;
    height: 132px;
    background: var(--magenta);
    color: var(--text-white);
    font-size: 76px;
    transform: rotate(-6deg);
  }
</style>
</head>
<body>
  <main class="poster">
    <div class="poster__art">
      <div class="poster__backdrop" role="img" aria-label="Swirling teal and lime ribbons with soft heart shapes"></div>
      <div class="poster__family" role="img" aria-label="Silhouettes of two parents holding a baby"></div>

      <p class="line line--came">We came here as a</p>
      <p class="tag tag--couple">couple</p>

      <p class="line line--left">We left as a</p>
      <p class="tag tag--family">family</p>
    </div>
  </main>
</body>
</html>
```